Bus Bench Ad Design Needed

Hi there. We would like to design an eye catching bus bench ad! The information that we would like to have on it is found below:

- Our logo which is attached below. We would this to take up at least half of the bus bench.
- Our phone number in bold, very visible to see. 555-318-2694. White numbers on an eye catching colored background.
- Our web address : www.SplitEase472.example
- A "Ring Otto" phrase in a black circle with yellow bold letters. Want the "Ring Otto" to be somewhat angled. We are thinking that the "Ring Otto" should be directly below the image in our logo.
- Our tag line we want somewhere in here as well which is "Divorce made easy - at a price you'll like!"

```html
<!DOCTYPE html>
<html lang="en">
<head>
<meta charset="utf-8">
<title>SplitEase Bench Ad</title>
<link rel="stylesheet" href="https://fonts.googleapis.com/css2?family=Marcellus&family=Mulish:wght@500&family=Montserrat:wght@700&family=Bebas+Neue&family=Roboto:ital,wght@1,900&family=Roboto+Condensed:ital,wght@1,700&display=swap">
<style>
  :root {
    --page: #b4b4b4;
    --paper: #ffffff;
    --ink: #111111;
    --brand-blue: #1b80c4;
    --accent-yellow: #fff200;
    --divider: #9a9a9a;
  }
  html, body {
    margin: 0;
    width: 1200px;
    height: 960px;
    overflow: hidden;
    background: var(--page);
  }
  .stage {
    position: relative;
    width: 1200px;
    height: 960px;
  }
  .bench-ad {
    position: absolute;
    left: 30px;
    top: 330px;
    width: 1348px;
    height: 356px;
    transform: scale(0.8457);
    transform-origin: top left;
    background: var(--paper);
    overflow: hidden;
  }
  .ad-shapes {
    position: absolute;
    inset: 0;
    width: 1348px;
    height: 356px;
  }
  .brand-mark {
    position: absolute;
    left: 56px;
    top: 48px;
    width: 110px;
    height: 110px;
    background: var(--brand-blue);
  }
  .brand-divider {
    position: absolute;
    left: 212px;
    top: 44px;
    width: 3px;
    height: 124px;
    background: var(--divider);
  }
  .brand-name {
    position: absolute;
    left: 228px;
    top: 28px;
    margin: 0;
    font: 400 104px/1 "Marcellus", serif;
    letter-spacing: 2px;
    color: var(--brand-blue);
    white-space: nowrap;
  }
  .brand-descriptor {
    position: absolute;
    left: 232px;
    top: 128px;
    margin: 0;
    font: 500 44px/1 "Mulish", sans-serif;
    color: var(--ink);
    white-space: nowrap;
  }
  .call-out {
    position: absolute;
    left: 1040px;
    top: 16px;
    margin: 0;
    font: italic 900 78px/0.86 "Roboto", sans-serif;
    color: var(--accent-yellow);
    text-transform: uppercase;
    transform: rotate(-4deg);
    white-space: nowrap;
  }
  .rule {
    position: absolute;
    left: 0;
    height: 4px;
    background: var(--ink);
  }
  .rule-top { top: 196px; width: 714px; }
  .rule-bottom { top: 254px; width: 706px; }
  .tagline {
    position: absolute;
    left: 36px;
    top: 206px;
    margin: 0;
    font: italic 700 37px/1 "Roboto Condensed", sans-serif;
    color: var(--ink);
    white-space: nowrap;
  }
  .tagline-accent { color: var(--brand-blue); }
  .web-address {
    position: absolute;
    left: 44px;
    top: 292px;
    margin: 0;
    font: 700 40px/1 "Montserrat", sans-serif;
    color: var(--paper);
    white-space: nowrap;
  }
  .phone {
    position: absolute;
    left: 730px;
    top: 214px;
    width: 600px;
    margin: 0;
    text-align: center;
    font: 400 128px/1 "Bebas Neue", sans-serif;
    letter-spacing: 1px;
    color: var(--accent-yellow);
    white-space: nowrap;
  }
</style>
</head>
<body>
<main class="stage">
  <section class="bench-ad">
    <svg class="ad-shapes" viewBox="0 0 1348 356" aria-hidden="true">
      <polygon points="0,270 700,270 672,356 0,356" fill="var(--brand-blue)"/>
      <polygon points="714,196 1348,196 1348,356 672,356" fill="var(--ink)"/>
      <circle cx="1142" cy="-14" r="210" fill="none" stroke="var(--brand-blue)" stroke-width="5"/>
      <circle cx="1142" cy="-14" r="200" fill="var(--ink)"/>
    </svg>

    <div class="brand-mark"></div>
    <div class="brand-divider"></div>
    <h1 class="brand-name">SPLITEASE</h1>
    <p class="brand-descriptor">Non-Lawyer Documents Service</p>

    <p class="call-out">Ring<br>Otto</p>

    <div class="rule rule-top"></div>
    <p class="tagline">Divorce made easy - <span class="tagline-accent">at a price you'll like!</span></p>
    <div class="rule rule-bottom"></div>

    <p class="web-address">www.SplitEase472.example</p>
    <p class="phone">555-318-2694</p>
  </section>
</main>
</body>
</html>
```